Business Card Design for The Lending Nook Inc.

We need a business card design for our mortgage company: "The Lending Nook Inc."

Need to have Social Media Account on there as a possibility

Industry/Entity Type

Business

```html
<!DOCTYPE html>
<html lang="en">
<head>
<meta charset="utf-8">
<title>The Lending Nook Inc. — Business Card</title>
<link rel="stylesheet" href="https://fonts.googleapis.com/css2?family=Open+Sans:wght@600;700&family=PT+Serif:wght@700&display=swap">
<style>
  :root {
    --backdrop: #f5ece3;
    --card-dark: #232c36;
    --pattern-dark: #28323d;
    --band-sky: #56b6d9;
    --band-light: #5ccff3;
    --band-mid: #00a6e4;
    --band-deep: #0077c2;
    --brand-blue: #0a5aa8;
    --icon-blue: #00b4ef;
    --ink-grey: #3d3d3d;
    --white: #ffffff;
  }
  * { margin: 0; padding: 0; box-sizing: border-box; }
  html, body { width: 1200px; height: 1001px; overflow: hidden; }
  body { background: var(--backdrop); position: relative; }

  .card { position: absolute; width: 612px; overflow: hidden; }

  /* Front */
  .card-front { left: 68px; top: 48px; height: 352px; background: var(--card-dark); }
  .front-texture { position: absolute; left: 150px; top: 0; width: 312px; height: 295px; background: linear-gradient(180deg, var(--pattern-dark), var(--card-dark)); }
  .front-brand-band { position: absolute; left: -2px; top: 107px; width: 616px; height: 98px; background: var(--band-sky); display: flex; align-items: center; justify-content: center; gap: 14px; }
  .brand-dot { width: 26px; height: 26px; border-radius: 50%; background: var(--brand-blue); }
  .brand-name { font-family: "Open Sans", sans-serif; font-weight: 700; color: var(--brand-blue); white-space: nowrap; }
  .front-brand-band .brand-name { font-size: 32px; }
  .accent-band { position: absolute; left: 0; width: 612px; background: linear-gradient(90deg, var(--band-deep) 0%, var(--band-mid) 12%, var(--band-light) 28%, var(--band-light) 72%, var(--band-mid) 88%, var(--band-deep) 100%); }
  .card-front .accent-band { top: 295px; height: 57px; }
  .front-links { position: absolute; left: 0; right: 0; top: 322px; text-align: center; font-family: "Open Sans", sans-serif; font-weight: 600; font-size: 12px; letter-spacing: 2px; color: var(--white); }
  .front-links .social { margin-left: 18px; }

  /* Back */
  .card-back { left: 446px; top: 490px; height: 348px; background: var(--white); }
  .back-header { position: absolute; left: 0; top: 0; width: 612px; height: 110px; }
  .back-header .brand { position: absolute; left: 32px; top: 40px; display: flex; align-items: center; gap: 8px; }
  .back-header .brand-dot { width: 18px; height: 18px; }
  .back-header .brand-name { font-size: 20px; }
  .person { position: absolute; right: 30px; top: 36px; text-align: right; font-family: "PT Serif", serif; font-weight: 700; }
  .person-name { font-size: 27px; line-height: 1; color: var(--brand-blue); }
  .person-title { font-size: 15px; line-height: 1.1; color: var(--ink-grey); }
  .card-back .accent-band { top: 110px; height: 50px; }
  .contact-panel { position: absolute; left: 0; top: 160px; width: 612px; height: 165px; background: var(--card-dark); }
  .contact-texture { position: absolute; left: 180px; top: 0; width: 260px; height: 165px; background: linear-gradient(180deg, var(--pattern-dark), var(--card-dark)); }
  .contact-item { position: absolute; top: 44px; text-align: center; font-family: "PT Serif", serif; font-weight: 700; font-size: 15px; color: var(--white); white-space: nowrap; }
  .contact-item svg { display: block; margin: 0 auto 20px; height: 32px; }
  .contact-email { left: 0; width: 217px; }
  .contact-phone { left: 217px; width: 182px; }
  .contact-address { left: 399px; width: 179px; }
  .divider { position: absolute; top: 13px; width: 2px; height: 129px; background: var(--white); }
  .divider-1 { left: 216px; }
  .divider-2 { left: 398px; }
  .back-footer { position: absolute; left: 0; top: 325px; width: 612px; height: 23px; background: var(--band-deep); }
</style>
</head>
<body>

<section class="card card-front">
  <div class="front-texture" role="img" aria-label="Subtle dark chevron texture"></div>
  <div class="front-brand-band">
    <span class="brand-dot"></span>
    <span class="brand-name">The Lending Nook Inc.</span>
  </div>
  <div class="accent-band" role="img" aria-label="Faceted blue triangle pattern band"></div>
  <p class="front-links">WWW.YOURWEBSITE.COM<span class="social">@LENDINGNOOK</span></p>
</section>

<section class="card card-back">
  <header class="back-header">
    <div class="brand">
      <span class="brand-dot"></span>
      <span class="brand-name">The Lending Nook Inc.</span>
    </div>
    <div class="person">
      <p class="person-name">YOUR NAME</p>
      <p class="person-title">Designation</p>
    </div>
  </header>
  <div class="accent-band" role="img" aria-label="Faceted blue triangle pattern band"></div>
  <div class="contact-panel">
    <div class="contact-texture" role="img" aria-label="Subtle dark chevron texture"></div>
    <div class="contact-item contact-email">
      <svg viewBox="0 0 38 26" width="38"><rect x="0" y="0" width="38" height="26" fill="var(--icon-blue)"/><polyline points="1,1 19,15 37,1" fill="none" stroke="var(--card-dark)" stroke-width="2"/><line x1="1" y1="25" x2="14" y2="11" stroke="var(--card-dark)" stroke-width="1.5"/><line x1="24" y1="11" x2="37" y2="25" stroke="var(--card-dark)" stroke-width="1.5"/></svg>
      youremail@example.com
    </div>
    <div class="contact-item contact-phone">
      <svg viewBox="0 0 32 32" width="32"><path d="M7 2 L12 8 L9 12 C11 17 15 21 20 23 L24 20 L30 25 L26 30 C14 29 3 18 2 6 Z" fill="var(--icon-blue)"/></svg>
      123-456-789
    </div>
    <div class="contact-item contact-address">
      <svg viewBox="0 0 44 36" width="44"><polygon points="22,0 44,19 39,19 22,5 5,19 0,19" fill="var(--icon-blue)"/><polygon points="8,19 22,8 36,19 36,36 26,36 26,25 18,25 18,36 8,36" fill="var(--icon-blue)"/><rect x="31" y="3" width="4" height="9" fill="var(--icon-blue)"/></svg>
      your address and place
    </div>
    <span class="divider divider-1"></span>
    <span class="divider divider-2"></span>
  </div>
  <div class="back-footer"></div>
</section>

</body>
</html>
```